Business Card Design.

Life and Wellness Coach
www.brightpathwell.com
Want to use my name as the logo it could be the initials TRH or my full name. I want to trade mark me.
I like clean lines and simple designs, but it pops using the colors scheme (one or two colors) on the website.
I provide life and health coaching virtually and in person. My services include: Nutrition Response Testing, Allergy Elimination Testing, Wellness Coaching, Life Coaching. Life and Health Assessments, and I sell foundational health products and specialized nutrition. Use colors that represent healing and trust.
Target Market(s)
Women for the ages of 30 - 60
Industry/Entity Type
Health
Contact Information for Business Card
Tessa Ravenna Holloway
Life and Wellness Coach
tessa@coachtrh.com
www.brightpathwell.com
443-781-6392
Health is not an event it's a lifestyle (tag line or if you have a better tag line)

```html
<!DOCTYPE html>
<html lang="en">
<head>
<meta charset="utf-8">
<title>Tessa Ravenna Holloway – Business Card</title>
<link href="https://fonts.googleapis.com/css2?family=Petit+Formal+Script&family=Arimo:wght@400&display=swap" rel="stylesheet">
<style>
  :root {
    --bg: #e4e4e6;
    --card: #f7fbfb;
    --ink: #1b1b1b;
    --accent: #b3306b;
    --photo-hair: #4a2620;
    --photo-dark: #22141a;
    --photo-blue: #2a3a8c;
  }
  * { margin: 0; padding: 0; box-sizing: border-box; }
  html, body { width: 1200px; height: 960px; overflow: hidden; }
  body {
    background: var(--bg);
    position: relative;
    font-family: "Arimo", Arial, sans-serif;
    color: var(--ink);
  }
  .card {
    position: absolute;
    left: 250px;
    width: 700px;
    height: 400px;
    background: var(--card);
    overflow: hidden;
    box-shadow: 0 6px 18px rgba(0,0,0,0.18);
  }
  .card--back { top: 50px; }
  .card--front { top: 510px; }

  /* back */
  .tagline {
    position: absolute;
    left: 90px;
    top: 184px;
    font-family: "Petit Formal Script", cursive;
    font-size: 25px;
    font-weight: 400;
    white-space: nowrap;
  }
  .tagline-rule {
    position: absolute;
    left: 0;
    right: 0;
    top: 228px;
    height: 4px;
    background: var(--accent);
  }

  /* front */
  .portrait {
    position: absolute;
    left: 0;
    top: 0;
    width: 700px;
    height: 400px;
  }
  .identity {
    position: absolute;
    left: 320px;
    top: 118px;
  }
  .identity__name {
    font-family: "Petit Formal Script", cursive;
    font-size: 22px;
    font-weight: 400;
    white-space: nowrap;
  }
  .identity__title {
    font-size: 15px;
    margin-top: 4px;
  }
  .contacts {
    position: absolute;
    left: 430px;
    top: 258px;
    list-style: none;
  }
  .contacts__item {
    display: flex;
    align-items: center;
    gap: 12px;
    font-size: 16px;
    height: 30px;
    white-space: nowrap;
  }
  .contacts__icon {
    width: 24px;
    height: 22px;
    background: var(--accent);
    border-radius: 3px;
    display: flex;
    align-items: center;
    justify-content: center;
  }
</style>
</head>
<body>

<section class="card card--back" aria-label="Business card back">
  <p class="tagline">Health is not an event it's a lifestyle</p>
  <div class="tagline-rule"></div>
</section>

<section class="card card--front" aria-label="Business card front">
  <svg class="portrait" viewBox="0 0 700 400" role="img" aria-label="Portrait photograph of the coach, smiling, with shoulder-length auburn hair">
    <defs>
      <linearGradient id="portraitTone" x1="0" y1="0" x2="1" y2="1">
        <stop offset="0" stop-color="var(--photo-dark)"/>
        <stop offset="0.55" stop-color="var(--photo-hair)"/>
        <stop offset="1" stop-color="var(--photo-blue)"/>
      </linearGradient>
    </defs>
    <path d="M0,170 C90,120 220,140 270,240 C295,290 300,350 292,400 L0,400 Z" fill="url(#portraitTone)"/>
    <path d="M0,170 C90,120 220,140 270,240 C295,290 300,350 292,400" fill="none" stroke="var(--accent)" stroke-width="4"/>
  </svg>

  <div class="identity">
    <h1 class="identity__name">Tessa Ravenna Holloway</h1>
    <p class="identity__title">Life and Wellness Coach</p>
  </div>

  <ul class="contacts">
    <li class="contacts__item">
      <span class="contacts__icon">
        <svg width="14" height="14" viewBox="0 0 24 24"><path fill="#fff" d="M6.6 10.8a15 15 0 0 0 6.6 6.6l2.2-2.2c.3-.3.7-.4 1-.2 1.1.4 2.3.6 3.6.6.6 0 1 .4 1 1V20c0 .6-.4 1-1 1C10.6 21 3 13.4 3 4c0-.6.4-1 1-1h3.5c.6 0 1 .4 1 1 0 1.3.2 2.5.6 3.6.1.3 0 .7-.2 1z"/></svg>
      </span>
      443-781-6392
    </li>
    <li class="contacts__item">
      <span class="contacts__icon">
        <svg width="14" height="14" viewBox="0 0 24 24" fill="none" stroke="#fff" stroke-width="2"><circle cx="12" cy="12" r="9"/><path d="M3 12h18M12 3c3 3 3 15 0 18M12 3c-3 3-3 15 0 18"/></svg>
      </span>
      www.brightpathwell.com
    </li>
    <li class="contacts__item">
      <span class="contacts__icon">
        <svg width="14" height="12" viewBox="0 0 24 18" fill="none" stroke="#fff" stroke-width="2"><rect x="1" y="1" width="22" height="16"/><path d="M1 1l11 9 11-9"/></svg>
      </span>
      tessa@coachtrh.com
    </li>
  </ul>
</section>

</body>
</html>
```